Baby Adoption Announcement

I'm looking for a simple, understated and modern baby adoption announcement.

The baby is a boy, but I don't want anything that is blue or particularly boyish. No storks, baby baskets, rattles, or traditional baby announcement designs. No cutesy or busy designs.

Should measure 5.25 x 8.25 inches to fit in an A9 envelope.

Simple graphics MIGHT include birds, grasses, trees, rivers. I'm open to other ideas. Text can be a single color or multi colored. Graphics are not mandatory.

Since this is text heavy, I'd like the designer to be REALLY GOOD at choosing fonts and typesetting.

Text should read:

Memory answers us bright on your face—
Impossibly, we spoke and were silent
Together before all of this. (in italics)

Cornelius Tobias Pelter Quist
Born on March 16, 2012 in Boston, MA
and entrusted to us by his birthmother, Gwenda.

Named Cornelius, which means God is with us, after Gwenda’s grandfather &
Tobias, after Toby and St. Tobias of Karvel

• Should measure 5.25 x 8.25 inches to fit in A9 envelope.

• The baby is a boy, but I don't want anything that is blue or particularly boyish. No storks, baby baskets, rattles, or traditional baby announcement designs. Nothing cutesy or busy.

```html
<!DOCTYPE html>
<html lang="en">
<head>
<meta charset="utf-8">
<title>Cornelius Tobias Pelter Quist – Adoption Announcement</title>
<link rel="stylesheet" href="https://fonts.googleapis.com/css2?family=Marcellus&family=Marcellus+SC&family=Petit+Formal+Script&display=swap">
<style>
  :root {
    --page: #fdf0e8;
    --card: #8b5232;
    --coral: #d4705f;
    --panel: #f1e6d5;
    --ink: #3f3a36;
    --wine: #8a2a3c;
    --trail: rgba(243, 230, 214, 0.10);
    --elephant: rgba(200, 138, 62, 0.85);
    --elephant-fade: rgba(200, 138, 62, 0);
    --dragonfly: rgba(212, 112, 95, 0.9);
    --dragonfly-fade: rgba(212, 112, 95, 0);
  }
  * { margin: 0; padding: 0; box-sizing: border-box; }
  html, body { width: 1200px; height: 897px; overflow: hidden; background: var(--page); }
  .canvas { position: relative; width: 1200px; height: 897px; }
  .card {
    position: absolute; left: 21px; top: 80px; width: 1147px; height: 743px;
    background: var(--card);
    box-shadow: 4px 5px 9px rgba(60, 30, 15, 0.45);
  }
  .card-frame {
    position: absolute; left: 34px; top: 96px; width: 1114px; height: 710px;
    border: 8px solid var(--coral);
    box-shadow: 2px 3px 5px rgba(40, 20, 10, 0.35);
  }
  .trail-art {
    position: absolute; border-radius: 50%;
    background: radial-gradient(closest-side, var(--trail), rgba(243, 230, 214, 0));
  }
  .trail-art.loop { left: 48px; top: 108px; width: 420px; height: 320px; }
  .trail-art.swirl { left: 975px; top: 370px; width: 170px; height: 150px; }
  .message-panel {
    position: absolute; left: 297px; top: 180px; width: 581px; height: 536px;
    background: var(--panel);
    border-radius: 46px;
    box-shadow: 3px 4px 8px rgba(50, 25, 10, 0.45);
  }
  .panel-border { position: absolute; left: 293px; top: 176px; }
  .message {
    position: absolute; left: 297px; top: 180px; width: 581px;
    text-align: center; color: var(--ink);
    font-family: "Marcellus", serif;
  }
  .verse {
    margin-top: 66px;
    font-family: "Petit Formal Script", cursive;
    font-size: 24px; line-height: 38px; color: var(--ink);
  }
  .child-name {
    margin-top: 30px;
    font-family: "Marcellus SC", serif; font-weight: 400;
    font-size: 27px; letter-spacing: 1px; color: var(--wine);
  }
  .details { font-size: 22px; line-height: 36px; }
  .details .birthmother {
    font-family: "Petit Formal Script", cursive; color: var(--wine); font-size: 20px;
  }
  .naming { margin-top: 26px; font-size: 22px; line-height: 37px; }
  .accent {
    font-family: "Marcellus SC", serif; color: var(--wine);
    text-transform: lowercase; font-variant: small-caps; letter-spacing: 0.8px;
    font-size: 1.08em;
  }
  .elephant-art {
    position: absolute; left: 84px; top: 530px; width: 222px; height: 250px;
    border-radius: 50%;
    background: radial-gradient(closest-side, var(--elephant) 55%, var(--elephant-fade));
  }
  .dragonfly-art {
    position: absolute; left: 1035px; top: 368px; width: 90px; height: 110px;
    border-radius: 50%;
    background: radial-gradient(closest-side, var(--dragonfly) 45%, var(--dragonfly-fade));
  }
</style>
</head>
<body>
<div class="canvas">
  <div class="card"></div>
  <div class="card-frame"></div>

  <div class="trail-art loop" role="img" aria-label="Dotted stitched trail looping across the upper left of the card"></div>
  <div class="trail-art swirl" role="img" aria-label="Dotted stitched swirl around the dragonfly"></div>

  <div class="message-panel"></div>
  <svg class="panel-border" width="589" height="544" viewBox="0 0 589 544" aria-hidden="true">
    <rect x="4" y="4" width="581" height="536" rx="46" fill="none"
          stroke="var(--coral)" stroke-width="8" stroke-dasharray="22 14"/>
  </svg>

  <div class="message">
    <p class="verse">Memory answers us bright on your face<br>Impossibly, we spoke and were silent<br>Together before all of this</p>
    <h1 class="child-name">Cornelius Tobias Pelter Quist</h1>
    <p class="details">Born on March 16, 2012 in Boston, MA<br>and entrusted to us by his birthmother, <span class="birthmother">Gwenda</span>.</p>
    <p class="naming">Named Cornelius, which means <span class="accent">God is with us</span><br>after Gwenda’s grandfather &amp;<br><span class="accent">Tobias</span>, after Toby and <span class="accent">St. Tobias of Karvel</span></p>
  </div>

  <div class="elephant-art" role="img" aria-label="Illustration of a little boy riding a tan spotted elephant"></div>
  <div class="dragonfly-art" role="img" aria-label="Illustration of a coral dragonfly"></div>
</div>
</body>
</html>
```